my website is tabellepiece.com. (brand name is ta belle pièce) This is just a template that i have choose for. The content and the pictures are not about my business just the template.
I would like to have 4 pages for now. 1 homepage, which will be an overview for all pages, it is right now in this way. It will directly highlight my story. My website will tell an exclusive story about details which makes the difference and will make people happy with very small things. It will be art related but very stylish as well. I also want to have a event agenda on my homepage where people can see where my next event is. Page 2 my blog, where I will write weekly about mindset, lifestyle and details. Inspiration place for people who are looking for unique and exclusive approaches in life. Page 3 shop, where I will sell my stuff which is handmade and unique, it will be limited edition stuff. Mostly I will make the designs from marbling art, which I am a teacher for. (https://www.vidorastream.com/watch?v=Kq7TbWm2Xa) check this video out for more. Page 4 is book page. Here people will be able to book private or group classes for marbling art (check the video). I have already a community of more than 500 people on join ring, which will be my public as well. I wanna implement the join ring button on this page as well. to be able to track.

This is about my website. I also need a logo for my brand, which will suit my website and my goals.

I can also give you a reference website, which really like as structure and style;
https://www.brightmorrowco.com/products/the-daybook-organizer?ref=Xp4RtLm8QzVw2NbKc7HsJd9FgTy3MvEqBa6WnUoZr1LkPxYhGiCe5DsAtQfVbNj0HmRwKyXo8LcTpZaEsUv2GqDnIwMb

ta belle pièce

4 page

• I can also give you a reference website, which really like as structure and style;
• https://www.brightmorrowco.com/products/the-daybook-organizer?ref=Xp4RtLm8QzVw2NbKc7HsJd9FgTy3MvEqBa6WnUoZr1LkPxYhGiCe5DsAtQfVbNj0HmRwKyXo8LcTpZaEsUv2GqDnIwMb

```html
<!DOCTYPE html>
<html lang="en">
<head>
<meta charset="utf-8">
<title>ta belle pièce</title>
<link rel="stylesheet" href="https://fonts.googleapis.com/css2?family=Montserrat:wght@400;600;700&family=Open+Sans:wght@400;600&display=swap">
<style>
:root{
  --ink:#111111;
  --black:#000000;
  --white:#ffffff;
  --text:#555555;
  --muted:#8a8a8a;
  --rule:#cfcfcf;
  --line:#bdbdbd;
  --quote-bg:#262626;
  --head:Montserrat, Arial, sans-serif;
  --body:"Open Sans", Arial, sans-serif;
}
*{box-sizing:border-box;margin:0;padding:0}
html,body{width:1200px;height:4932px;overflow:hidden}
body{background:var(--white);font-family:var(--body);color:var(--text);position:relative}
section,header,footer{position:absolute;left:0;width:1200px}
.abs{position:absolute}
.center{left:0;width:1200px;text-align:center}
.h-title{font-family:var(--head);font-weight:700;letter-spacing:1px;color:var(--ink);font-size:17px}
.h-sub{font-family:var(--head);font-size:10px;letter-spacing:1px;color:var(--muted);margin-top:6px}
.h-rule{width:150px;height:1px;background:var(--rule);margin:12px auto 0}
.copy{font-size:11.5px;line-height:19px;color:var(--text)}
.btn{font-family:var(--head);font-size:10px;font-weight:600;letter-spacing:1px;display:flex;align-items:center;justify-content:center;border:1px solid var(--ink);color:var(--ink);background:var(--white);white-space:nowrap}

/* header */
.site-header{top:0;height:72px;background:var(--white)}
.brand{left:150px;top:20px;display:flex;align-items:center;gap:10px;font-family:var(--head);font-size:15px;font-weight:600;color:var(--ink);white-space:nowrap}
.brand-mark{width:14px;height:14px;border:1.5px solid var(--ink)}
.nav{top:29px;font-family:var(--head);font-size:12px;font-weight:600;letter-spacing:1px;color:var(--ink)}
.menu{left:1002px;top:27px}

/* hero */
.hero{top:72px;height:530px;background:linear-gradient(180deg,#5a3e56 0%,#3b3f44 22%,#262a2d 50%,#1d2022 100%)}
.hero-kicker{top:212px;font-family:var(--head);font-size:11px;font-weight:600;letter-spacing:1px;color:var(--white)}
.hero-rule{top:257px;left:570px;width:60px;height:1px;background:var(--white)}
.hero-title{top:278px;font-family:var(--head);font-size:30px;font-weight:600;line-height:52px;letter-spacing:1.5px;color:var(--white)}
.hero-btn{top:428px;left:515px;width:171px;height:43px;background:transparent;border-color:var(--white);color:var(--white);font-size:9px}

/* promo band */
.promo{top:602px;height:121px;background:var(--black)}
.promo-text{left:329px;top:53px;font-family:var(--head);font-size:10px;font-weight:600;letter-spacing:1px;color:var(--white);white-space:nowrap}
.promo-btn{left:740px;top:41px;width:148px;height:40px;border-radius:20px;border:none;font-size:10px}

/* beginning */
.story{top:723px;height:425px}
.story-body{left:161px;top:58px;width:385px}
.story-body .h-title{font-size:16px}
.story-body .h-sub{margin-top:5px;font-size:9px}
.story-dash{width:22px;height:1px;background:var(--ink);margin:14px 0 22px}
.story-body .copy{font-size:10.5px;line-height:17px;margin-bottom:14px}
.story-btn{left:161px;top:329px;width:148px;height:37px}
.story-photo{left:579px;top:0;width:473px;height:425px;background:linear-gradient(135deg,#8a5e63 0%,#b98a8c 45%,#6e4c55 100%)}

/* video */
.video{top:1148px;height:437px;background:linear-gradient(180deg,#4a2a30 0%,#2a2526 35%,#1c1d1f 70%,#3a3436 100%)}
.video-title{top:166px;font-family:var(--head);font-size:15px;font-weight:700;letter-spacing:1px;color:var(--white)}
.play{left:571px;top:214px}

/* shop */
.shop{top:1585px;height:1111px}
.shop-head{top:50px}
.shop-copy{top:168px;left:350px;width:500px;text-align:center}
.tabs{top:279px;left:0;width:1200px}
.tab{position:absolute;height:36px;top:0;font-size:9px}
.tab.active{background:var(--ink);color:var(--white)}
.tile{position:absolute;width:277px;height:279px}
.more-btn{left:536px;top:1016px;width:131px;height:36px;font-size:9px}

/* testimonial */
.quote{top:2696px;height:296px;background:var(--quote-bg)}
.quote-mark{left:579px;top:61px}
.quote-text{top:163px;font-family:var(--head);font-size:13px;font-weight:600;line-height:27px;letter-spacing:1px;color:var(--white)}
.quote-by{top:230px;font-family:var(--head);font-size:9px;font-weight:600;letter-spacing:1px;color:var(--white)}

/* about */
.about{top:2992px;height:796px}
.about-head{top:55px}
.about-copy{top:178px;left:350px;width:500px;text-align:center}
.member{position:absolute;top:283px;width:204px;height:263px}
.member-photo{width:204px;height:225px}
.member-name{height:38px;background:var(--ink);color:var(--white);font-family:var(--head);font-size:9px;font-weight:600;letter-spacing:.5px;display:flex;align-items:center;justify-content:center}
.member-name.light{background:var(--white);color:var(--ink)}
.about-col{position:absolute;top:600px;width:270px}
.about-col h3{font-family:var(--head);font-size:11px;font-weight:700;letter-spacing:.5px;color:var(--ink);margin-bottom:22px}
.about-col .copy{font-size:10.5px;line-height:17px}

/* newsletter */
.newsletter{top:3788px;height:197px;background:var(--black)}
.news-title{left:237px;top:57px;font-family:var(--head);font-size:12px;font-weight:700;letter-spacing:1px;color:var(--white)}
.news-input{left:237px;top:92px;width:575px;height:37px;border:1px solid var(--muted);display:flex;align-items:center;gap:14px;padding-left:16px;font-family:var(--head);font-size:9px;font-weight:600;color:var(--white);letter-spacing:.5px}
.news-btn{left:835px;top:92px;width:128px;height:37px;border:none;font-size:9px}

/* contact */
.contact{top:3985px;height:677px}
.contact-head{top:52px}
.contact-copy{top:164px;left:350px;width:500px;text-align:center}
.info{position:absolute;top:272px;width:260px;text-align:center;font-size:10.5px;line-height:16px}
.info svg{display:block;margin:0 auto 10px}
.field{position:absolute;border:1px solid var(--line);font-size:10px;color:var(--muted);padding:10px 12px}
.submit{left:911px;top:579px;width:128px;height:37px;background:var(--black);color:var(--white);border:none;font-size:9px}

/* footer */
.site-footer{top:4662px;height:270px;background:var(--black)}
.social{top:150px;left:0;width:1200px;display:flex;justify-content:center;gap:22px}
.social span{width:12px;height:12px;border-radius:50%;background:var(--white)}
.legal{top:192px;font-family:var(--head);font-size:9px;font-weight:600;color:var(--white);letter-spacing:.5px}
</style>
</head>
<body>

<header class="site-header">
  <div class="abs brand"><span class="brand-mark"></span>ta belle pièce</div>
  <div class="abs nav" style="left:478px">HOME</div>
  <div class="abs nav" style="left:570px">BLOG</div>
  <div class="abs nav" style="left:662px">SHOP</div>
  <div class="abs nav" style="left:755px">BOOK</div>
  <svg class="abs menu" width="22" height="16" viewBox="0 0 22 16"><rect y="0" width="22" height="2.5" fill="#111"/><rect y="6.5" width="22" height="2.5" fill="#111"/><rect y="13" width="22" height="2.5" fill="#111"/></svg>
</header>

<section class="hero" role="img" aria-label="Marbling tray with floating paint patterns and colourful paint jars">
  <div class="abs center hero-kicker">ELEGANT BEAUTY IN AN ART FORM</div>
  <div class="hero-rule abs"></div>
  <div class="abs center hero-title">AN UNPARALLELED SELECTION<br>NEW ARRIVALS ARE HERE</div>
  <div class="abs btn hero-btn">CLICK TO SHOP NOW</div>
</section>

<section class="promo">
  <div class="abs promo-text">BEST ONLINE EBRU ART STORE NEAR YOU, SHOP NOW</div>
  <div class="abs btn promo-btn">SHOP NOW</div>
</section>

<section class="story">
  <div class="abs story-body">
    <div class="h-title">OUR BEGINNING</div>
    <div class="h-sub">CLOSER TO THE STARS</div>
    <div class="story-dash"></div>
    <p class="copy">Donec rutrum congue leo eget malesuada. Curabitur non nulla sit amet nisl tempus convallis quis ac lectus. Sed porttitor lectus nibh. Proin eget tortor risus. Nulla porttitor accumsan tincidunt.</p>
    <p class="copy">Curabitur aliquet quam id dui posuere blandit.<br>Nulla quis lorem ut libero malesuada feugiat. Donec rutrum congue leo eget malesuada. Curabitur aliquet quam id dui posuere blandit.</p>
  </div>
  <div class="abs btn story-btn">SEE PORTFOLIO</div>
  <div class="abs story-photo" role="img" aria-label="Hands drawing a marbled pattern on water with a stylus"></div>
</section>

<section class="video" role="img" aria-label="Video preview of a marbling class with patterned paper">
  <div class="abs center video-title">SEE OUR VIDEO</div>
  <svg class="abs play" width="58" height="58" viewBox="0 0 58 58"><circle cx="29" cy="29" r="29" fill="#fff"/><path d="M23 18 L41 29 L23 40 Z" fill="#111"/></svg>
</section>

<section class="shop">
  <div class="abs center shop-head">
    <div class="h-title">SHOP</div>
    <div class="h-sub">SHOP OUR BEST STORY SO FAR</div>
    <div class="h-rule"></div>
  </div>
  <p class="abs copy shop-copy">Donec rutrum congue leo eget malesuada. Curabitur non nulla sit amet nisl tempus convallis quis ac lectus. Sed porttitor lectus nibh. Proin eget tortor risus. Nulla porttitor accumsan tincidunt. Nulla porttitor accumsan tincidunt.</p>
  <div class="abs tabs">
    <div class="btn tab active" style="left:335px;width:105px">PRODUCT</div>
    <div class="btn tab" style="left:463px;width:129px">SHIPPING</div>
    <div class="btn tab" style="left:615px;width:125px">BULK ORDERS</div>
    <div class="btn tab" style="left:763px;width:98px">FAQS</div>
  </div>
  <div class="tile" style="left:161px;top:375px;background:linear-gradient(160deg,#3a3f3a,#8a4a3c 60%,#a9786a)" role="img" aria-label="Marbled paper drying beside paint bottles"></div>
  <div class="tile" style="left:460px;top:375px;background:linear-gradient(140deg,#b78d86,#8f5f63 55%,#c8a19a)" role="img" aria-label="Stylus shaping a pink marbling pattern"></div>
  <div class="tile" style="left:763px;top:375px;background:linear-gradient(140deg,#5e4d7a,#8f6c9a 50%,#d3c2d6)" role="img" aria-label="Purple floral marbling on water"></div>
  <div class="tile" style="left:161px;top:677px;background:linear-gradient(180deg,#5a4e48,#2b2d2f 45%,#1c1e20)" role="img" aria-label="Paint jars above a dark marbling tray"></div>
  <div class="tile" style="left:460px;top:677px;background:linear-gradient(180deg,#7a8a8a,#5fa39a 40%,#d06b7a 75%,#6aa58a)" role="img" aria-label="Finished floral marbled sheet in pink and green"></div>
  <div class="tile" style="left:763px;top:677px;background:linear-gradient(180deg,#5a4e48,#2b2d2f 45%,#1c1e20)" role="img" aria-label="Paint jars above a dark marbling tray"></div>
  <div class="abs btn more-btn">SEE MORE</div>
</section>

<section class="quote">
  <svg class="abs quote-mark" width="42" height="42" viewBox="0 0 42 42"><circle cx="21" cy="21" r="21" fill="#fff"/><path d="M13 25 q0-8 6-10 l1 2 q-3 1.5-3 4 h3 v6 h-7z M22 25 q0-8 6-10 l1 2 q-3 1.5-3 4 h3 v6 h-7z" fill="#111"/></svg>
  <div class="abs center quote-text">LOREM IPSUM DOLOR SIT, AD ETIAM SIT ONER<br>OL DEIAN BOST SIT EMIST.</div>
  <div class="abs center quote-by">WREN ASHFORD</div>
</section>

<section class="about">
  <div class="abs center about-head">
    <div class="h-title">ABOUT US</div>
    <div class="h-sub">WHO WE ARE</div>
    <div class="h-rule"></div>
  </div>
  <p class="abs copy about-copy">Donec rutrum congue leo eget malesuada. Curabitur non nulla sit amet nisl tempus convallis quis ac lectus. Sed porttitor lectus nibh. Proin eget tortor risus. Nulla porttitor accumsan tincidunt.</p>
  <div class="member" style="left:161px"><div class="member-photo" style="background:linear-gradient(180deg,#c9ccce,#9ea3a7)" role="img" aria-label="Portrait of a team member"></div><div class="member-name light">NOEL ASHFORD</div></div>
  <div class="member" style="left:388px"><div class="member-photo" style="background:linear-gradient(180deg,#6e7a86,#3f4a55)" role="img" aria-label="Portrait of a team member"></div><div class="member-name">NOEL ASHFORD</div></div>
  <div class="member" style="left:612px"><div class="member-photo" style="background:linear-gradient(180deg,#5b6f80,#2f3d4a)" role="img" aria-label="Portrait of a team member"></div><div class="member-name">NOEL ASHFORD</div></div>
  <div class="member" style="left:835px"><div class="member-photo" style="background:linear-gradient(180deg,#8a8f94,#3b3e42)" role="img" aria-label="Portrait of a team member"></div><div class="member-name">NOEL ASHFORD</div></div>
  <div class="about-col" style="left:161px"><h3>ABOUT US</h3><p class="copy">Donec rutrum congue leo eget malesuada. Curabitur non nulla sit amet nisl tempus convallis quis ac lectus. Sed porttitor lectus nibh. Proin eget tortor risus. Nulla porttitor accumsan tincidunt.</p></div>
  <div class="about-col" style="left:463px"><h3>WHO WE ARE</h3><p class="copy">Donec rutrum congue leo eget malesuada. Curabitur non nulla sit amet nisl tempus convallis quis ac lectus. Sed porttitor lectus nibh.</p></div>
  <div class="about-col" style="left:763px"><h3>HOW WE DO THIS</h3><p class="copy">Donec rutrum congue leo eget malesuada. Curabitur non nulla sit amet nisl tempus convallis quis ac lectus. Sed porttitor lectus nibh. Proin eget tortor risus.</p></div>
</section>

<section class="newsletter">
  <div class="abs news-title">SUBSCRIBE TO OUR NEWSLETTER</div>
  <div class="abs news-input"><svg width="14" height="10" viewBox="0 0 14 10"><rect x=".5" y=".5" width="13" height="9" fill="none" stroke="#fff"/><path d="M.5 .5 L7 6 L13.5 .5" fill="none" stroke="#fff"/></svg>EMAIL ADDRESS</div>
  <div class="abs btn news-btn">SUBSCRIBE</div>
</section>

<section class="contact">
  <div class="abs center contact-head">
    <div class="h-title">CONTACT US</div>
    <div class="h-sub">WE LOVE TALKING</div>
    <div class="h-rule"></div>
  </div>
  <p class="abs copy contact-copy">Donec rutrum congue leo eget malesuada. Curabitur non nulla sit amet nisl tempus convallis quis ac lectus. Sed porttitor lectus nibh. Proin eget tortor risus. Nulla porttitor accumsan tincidunt.</p>
  <div class="info" style="left:166px"><svg width="20" height="18" viewBox="0 0 20 18"><rect x="1" y="1" width="18" height="12" fill="none" stroke="#111" stroke-width="2"/><rect x="7" y="15" width="6" height="2" fill="#111"/></svg>hello@tabellepiece.com</div>
  <div class="info" style="left:472px"><svg width="20" height="18" viewBox="0 0 20 18"><path d="M10 1 L19 9 H16 V17 H12 V12 H8 V17 H4 V9 H1 Z" fill="#111"/></svg>4821 Maple Crest Lane<br>Brookfield, TX 70000</div>
  <div class="info" style="left:771px"><svg width="18" height="18" viewBox="0 0 18 18"><path d="M4 1 L7 1 L8 5 L6 7 Q8 11 11 12 L13 10 L17 11 L17 14 Q16 17 13 17 Q2 15 1 4 Q1 1 4 1Z" fill="#111"/></svg>+1 555 - 014 - 882</div>
  <div class="field" style="left:161px;top:395px;width:428px;height:39px">Subject*</div>
  <div class="field" style="left:161px;top:457px;width:428px;height:39px">Name*</div>
  <div class="field" style="left:161px;top:519px;width:428px;height:40px">Email*</div>
  <div class="field" style="left:608px;top:395px;width:431px;height:157px">Message</div>
  <div class="abs btn submit">SUBMIT</div>
</section>

<footer class="site-footer">
  <div class="abs social"><span></span><span></span><span></span><span></span><span></span></div>
  <div class="abs center legal">© 2017 - ta belle pièce. All Right Reserved</div>
</footer>

</body>
</html>
```